Website for a dog poop removal service.

The Fernwick Folks specializes in professional and hassle-free pet waste removal services, ensuring your yard stays clean, fresh, and safe for your family and pets. We take care of the dirty work, so you don’t have to, offering reliable, scheduled cleanups tailored to your needs. Let us help you reclaim your time and enjoy a spotless, stress-free outdoor space!
We will need the winning website to be transferred to our domain located at Valtorix. We would like to have the following web pages.
Home
About
Services
Contact Us
Client Portal
FAQ
Blog
Free Quote
The Free Quote webpage and client portal will need to be integrated with the following our account on the following website: tallowfen.com

```html
<!DOCTYPE html>
<html lang="en">
<head>
<meta charset="utf-8">
<title>The Fernwick Folks – Pet Waste Removal</title>
<link href="https://fonts.googleapis.com/css2?family=Chewy&family=Poppins:wght@400;500;600;700&display=swap" rel="stylesheet">
<style>
:root{
  --sky:#b3f0f5;
  --grass:#7cc64a;
  --grass-dark:#5aaa2e;
  --ink:#1d1d1d;
  --text:#2b2b2b;
  --muted:#8a8a8a;
  --brown:#a99886;
  --accent:#f28c28;
  --white:#ffffff;
  --card-border:#e6e6e6;
  --icon-bg:#e7f0fb;
}
*{box-sizing:border-box;margin:0;padding:0}
html,body{width:1200px;height:4380px;overflow:hidden}
body{position:relative;background:var(--white);font-family:'Poppins',sans-serif;color:var(--text)}
.abs{position:absolute}
.display{font-family:'Chewy',cursive;font-weight:400;color:var(--ink)}
.btn{position:absolute;display:flex;align-items:center;justify-content:center;border-radius:24px;font-weight:600;font-size:13px}
.btn-dark{background:var(--ink);color:var(--white)}
.btn-outline{border:2px solid var(--ink);color:var(--ink);background:var(--white)}
.visual{position:absolute}

/* header */
.hero-bg{left:0;top:0;width:1200px;height:780px;background:var(--sky)}
.brand{left:86px;top:40px;display:flex;align-items:center;gap:12px}
.brand-dot{width:44px;height:44px;border-radius:50%;background:var(--grass)}
.brand-name{font-weight:700;font-size:20px;color:var(--ink);line-height:1.1;width:130px}
.nav{left:413px;top:26px;width:709px;height:68px;background:var(--white);border-radius:34px 0 0 34px;display:flex;align-items:center;padding-left:32px;gap:28px;font-size:13px;font-weight:500;color:var(--ink)}
.nav .active{color:var(--accent)}
.nav .quote{margin-left:auto;margin-right:4px;background:var(--ink);color:var(--white);padding:14px 34px;border-radius:24px;font-weight:600;font-size:14px}

.hero-title{left:104px;top:222px;font-size:64px;line-height:70px;width:560px}
.hero-sub{left:106px;top:450px;font-size:14px}
.hero-photo{left:690px;top:160px;width:420px;height:490px;border-radius:40px;transform:rotate(3deg);background:linear-gradient(160deg,#b88c5a,#7ea24c 55%,#5e8d33)}
.hero-ball-a{left:660px;top:146px;width:74px;height:74px;border-radius:50%;background:var(--grass)}
.hero-ball-b{left:1060px;top:586px;width:72px;height:72px;border-radius:50%;background:#c9a48a}

/* benefits */
.benefits{left:0;top:730px;width:1200px;height:345px}
.benefits-title{left:0;top:800px;width:1200px;text-align:center;font-size:32px;color:var(--white)}
.benefit{top:893px;width:212px;height:107px;background:var(--white);border-radius:16px;display:flex;align-items:center;justify-content:center;text-align:center;font-family:'Chewy',cursive;font-size:17px;line-height:20px;color:var(--ink);padding-top:8px}
.benefit-icon{width:54px;height:54px;border-radius:50%;background:var(--ink);border:3px solid var(--white)}

/* about */
.about-photo{left:172px;top:1180px;width:422px;height:422px;border-radius:50%;background:linear-gradient(170deg,#9cc3e8,#7aa74e 55%,#4b8c2c)}
.about-dog{left:118px;top:1360px;width:150px;height:250px;border-radius:60px 60px 30px 30px;background:linear-gradient(#f3e2c4,#d9bc8d)}
.about-title{left:643px;top:1232px;font-size:40px}
.about-text{left:643px;top:1304px;width:418px;font-size:12.5px;line-height:20px;color:var(--text)}
.about-text p+p{margin-top:18px}

/* why */
.why-blob{left:0;top:1717px;width:470px;height:400px}
.why-dog{left:128px;top:1718px;width:340px;height:380px;border-radius:150px 150px 60px 60px;background:linear-gradient(#ffffff,#e9e2da);border:4px solid var(--ink)}
.why-title{left:503px;top:1735px;font-size:38px}
.why-item{width:290px;display:flex;gap:20px}
.why-icon{flex:none;width:104px;height:104px;margin-top:-8px;border-radius:50%;background:var(--icon-bg);display:flex;align-items:center;justify-content:center}
.why-item h3{font-family:'Chewy',cursive;font-weight:400;font-size:17px;color:var(--ink);line-height:20px}
.why-item p{font-size:12.5px;line-height:20px;margin-top:10px;color:#444}
.why-icon svg{width:54px;height:54px;fill:none;stroke:var(--ink);stroke-width:2}

/* services */
.services-band{left:0;top:2180px;width:1200px;height:562px}
.services-title{left:0;top:2246px;width:1200px;text-align:center;font-size:40px;color:var(--white)}
.service{top:2363px;width:224px;height:264px;background:var(--white);border-radius:22px;text-align:center;padding:100px 16px 0}
.service h3{font-family:'Chewy',cursive;font-weight:400;font-size:17px;color:var(--ink)}
.service p{font-size:12.5px;line-height:20px;margin-top:12px;color:#333}
.service-icon{width:118px;height:118px;border-radius:50%;background:var(--grass);border:5px solid var(--white);display:flex;align-items:center;justify-content:center}
.service-icon.dark{background:var(--ink)}
.service-icon svg{width:56px;height:56px;fill:none;stroke:var(--white);stroke-width:2}

/* faq */
.faq-title{left:0;top:2825px;width:1200px;text-align:center;font-size:40px}
.tabs{left:110px;top:2922px;width:980px;display:flex;align-items:center;justify-content:space-between;font-size:13px;color:var(--muted)}
.tabs .on{background:var(--ink);color:var(--white);font-weight:600;padding:12px 24px;border-radius:22px;position:relative}
.tabs .on::after{content:"";position:absolute;left:58px;bottom:-6px;width:56px;height:5px;border-radius:3px;background:var(--grass)}
.faq-open{left:116px;top:3012px;width:969px;height:136px;border-radius:18px;box-shadow:0 2px 14px rgba(0,0,0,.1);background:var(--white);padding:28px 40px}
.faq-open h3,.faq-row h3{font-size:19px;font-weight:500;color:var(--ink)}
.faq-open p{font-size:11.5px;line-height:19px;margin-top:12px;color:#444;width:860px}
.faq-row{left:139px;width:922px;height:88px;display:flex;align-items:center;justify-content:space-between;padding-left:16px}
.faq-row+.faq-row{border-top:1px solid #d8d8d8}
.caret{width:0;height:0;border-left:6px solid transparent;border-right:6px solid transparent}
.caret.up{border-bottom:7px solid #bbb}
.caret.down{border-top:7px solid var(--ink)}

/* cta */
.cta-bg{left:0;top:3440px;width:1200px;height:540px;background:var(--sky)}
.cta-title{left:118px;top:3588px;font-size:62px;line-height:70px}
.cta-sub{left:119px;top:3740px;font-size:18px;line-height:28px;color:var(--ink)}
.cta-house{left:650px;top:3600px;width:520px;height:340px;background:linear-gradient(#b48a6e,#8c5f45 40%,#c9a089);border-radius:6px}
.cta-dog{left:640px;top:3700px;width:220px;height:250px;border-radius:100px 100px 40px 40px;background:linear-gradient(#ffffff,#e9e2da);border:4px solid var(--ink)}
.cta-bush{left:20px;top:3805px;width:130px;height:90px;border-radius:60px 60px 10px 10px;background:var(--grass-dark)}

/* footer */
.footer{left:0;top:3930px;width:1200px;height:390px}
.foot-brand{left:110px;top:4070px;width:160px;text-align:center}
.foot-brand .dot{width:110px;height:110px;border-radius:50%;background:var(--white);margin:0 auto 14px;opacity:.9}
.foot-brand span{font-weight:700;font-size:18px;color:var(--white);line-height:22px}
.foot-col h4{font-family:'Chewy',cursive;font-weight:400;font-size:23px;color:var(--white)}
.foot-links{margin-top:22px;font-size:13px;line-height:16.5px;color:var(--white)}
.contact{display:flex;gap:12px;margin-top:18px;color:var(--white);font-size:12.5px;line-height:16px}
.contact b{font-weight:600}
.contact .ic{flex:none;width:26px;height:26px;border-radius:50%;background:#c8957a;display:flex;align-items:center;justify-content:center}
.contact .ic svg{width:13px;height:13px;fill:var(--white)}
.socials{display:flex;gap:14px;margin-top:18px}
.socials span{width:18px;height:18px;border-radius:50%;background:var(--white)}
.copyright{left:0;top:4345px;width:1200px;text-align:center;font-size:12.5px;color:var(--ink)}
</style>
</head>
<body>

<!-- hero -->
<div class="abs hero-bg"></div>
<div class="abs brand"><span class="brand-dot"></span><span class="brand-name">The Fernwick Folks</span></div>
<nav class="abs nav">
  <span class="active">Home</span><span>About</span><span>Services ▾</span><span>Client Portal</span><span>FAQ</span><span>Blog</span><span>Contact</span>
  <span class="quote">Free Quote</span>
</nav>
<h1 class="abs display hero-title">Keeping Your Yard Clean, Fresh, and Hassle-Free!"</h1>
<p class="abs hero-sub">Professional pet waste removal services tailored to your needs."</p>
<a class="btn btn-dark" style="left:104px;top:507px;width:221px;height:44px">Get a Free Quote Today!</a>
<a class="btn btn-outline" style="left:345px;top:507px;width:269px;height:44px">Schedule Your First Cleanup Now!"</a>
<div class="visual hero-photo" role="img" aria-label="Photo of a happy family playing football with their child on a clean back lawn"></div>
<div class="abs hero-ball-a"></div>
<div class="abs hero-ball-b"></div>

<!-- key benefits -->
<svg class="abs benefits" viewBox="0 0 1200 345" preserveAspectRatio="none" aria-hidden="true">
  <path d="M0 40 Q300 20 600 40 T1200 40 V320 Q900 345 600 330 T0 335 Z" fill="#7cc64a"/>
  <path d="M0 40 Q300 20 600 40 T1200 40 V70 Q600 55 0 70 Z" fill="#6cb83d"/>
  <path d="M0 250 Q300 235 600 250 T1200 250 V320 Q900 345 600 330 T0 335 Z" fill="#5aaa2e"/>
</svg>
<h2 class="abs display benefits-title">Key Benefits</h2>
<div class="abs benefit" style="left:128px">Reliable, scheduled<br>cleanups</div>
<div class="abs benefit" style="left:374px">Safe for pets<br>and family</div>
<div class="abs benefit" style="left:621px">Affordable and<br>hassle-free</div>
<div class="abs benefit" style="left:867px">Environmentally<br>responsible disposal</div>
<span class="abs benefit-icon" style="left:116px;top:870px"></span>
<span class="abs benefit-icon" style="left:362px;top:870px"></span>
<span class="abs benefit-icon" style="left:609px;top:870px"></span>
<span class="abs benefit-icon" style="left:855px;top:870px"></span>

<!-- about -->
<div class="visual about-photo" role="img" aria-label="Photo of a worker clearing yard waste from a lawn in front of a house"></div>
<div class="visual about-dog" role="img" aria-label="Photo of a fluffy cream-coloured dog sitting"></div>
<h2 class="abs display about-title">About Fernwick Folks</h2>
<div class="abs about-text">
  <p>We're passionate about making life easier for pet owners. Our professional team is dedicated to ensuring your yard stays clean, healthy, and stress-free. With flexible scheduling, affordable rates, and top-notch customer service, we make pet ownership even more enjoyable.</p>
  <p>The Fernwick Folks specializes in professional and hassle-free pet waste removal services, ensuring your yard stays clean, fresh, and safe for your family and pets. We take care of the dirty work, so you don't have to, offering reliable, scheduled cleanups tailored to your needs. Let us help you reclaim your time and enjoy a spotless, stress-free outdoor space!</p>
</div>

<!-- why choose us -->
<svg class="abs why-blob" viewBox="0 0 470 400" aria-hidden="true">
  <path d="M0 20 Q120 0 240 40 Q330 80 360 200 Q380 300 470 330 Q420 395 240 385 Q100 380 0 400 Z" fill="#7cc64a"/>
</svg>
<div class="visual why-dog" role="img" aria-label="Cartoon dog mascot in a green scarf holding a pooper scooper"></div>
<h2 class="abs display why-title">Why Choose Us?</h2>
<div class="abs why-item" style="left:493px;top:1830px">
  <span class="why-icon"><svg viewBox="0 0 24 24"><circle cx="12" cy="12" r="4"/><path d="M12 2v3M12 19v3M2 12h3M19 12h3M5 5l2 2M17 17l2 2M5 19l2-2M17 7l2-2"/></svg></span>
  <div><h3>Reliable Service</h3><p>Always on time, always thorough</p></div>
</div>
<div class="abs why-item" style="left:796px;top:1830px">
  <span class="why-icon"><svg viewBox="0 0 24 24"><path d="M6 20c0-6 3-10 7-11l3-4 1 4c2 1 3 3 2 5l-3 1-2 5"/></svg></span>
  <div><h3>Pet &amp; Eco-Friendly</h3><p>Safe disposal methods and eco-conscious practices.</p></div>
</div>
<div class="abs why-item" style="left:493px;top:1993px">
  <span class="why-icon"><svg viewBox="0 0 24 24"><path d="M4 11h4v9H4zM8 12l4-7c1 0 2 1 2 2l-1 4h6l-1 9H8"/></svg></span>
  <div><h3>Satisfaction<br>Guaranteed</h3><p>We're not happy unless you're happy!</p></div>
</div>
<div class="abs why-item" style="left:796px;top:1993px">
  <span class="why-icon"><svg viewBox="0 0 24 24"><path d="M12 21s-6-6-6-11a6 6 0 0 1 12 0c0 5-6 11-6 11z"/><circle cx="12" cy="10" r="2"/></svg></span>
  <div><h3>Locally Owned &amp;<br>Operated</h3><p>Supporting our community, one yard at a time.</p></div>
</div>

<!-- services -->
<svg class="abs services-band" viewBox="0 0 1200 562" preserveAspectRatio="none" aria-hidden="true">
  <defs><linearGradient id="svcFill" x1="0" y1="0" x2="0" y2="1"><stop offset="0" stop-color="#a99886"/><stop offset=".7" stop-color="#b3a288"/><stop offset="1" stop-color="#9c9a70"/></linearGradient></defs>
  <path d="M0 20 Q300 0 600 18 T1200 10 V545 Q900 562 600 548 T0 552 Z" fill="url(#svcFill)"/>
</svg>
<h2 class="abs display services-title">Our Services Tailored to Your Needs</h2>
<div class="abs service" style="left:116px"><h3>Weekly Cleanups</h3><p>Keep your yard spotless with our regular cleanup services. Ideal for maintaining a fresh and clean outdoor space.</p></div>
<div class="abs service" style="left:366px"><h3>One-Time Cleanups</h3><p>Need help before a special event or after a busy week? We've got you covered with our one-time cleanup service.</p></div>
<div class="abs service" style="left:612px"><h3>Custom Schedules</h3><p>Choose a schedule that fits your lifestyle. We offer flexible options to ensure your yard stays pristine.</p></div>
<div class="abs service" style="left:860px"><h3>Commercial Services</h3><p>Perfect for parks, apartment complexes, and other dog-friendly spaces. Let us handle the mess while you focus on your property</p></div>
<span class="abs service-icon" style="left:169px;top:2322px"><svg viewBox="0 0 24 24"><rect x="3" y="5" width="18" height="15" rx="2"/><path d="M3 9h18M8 3v4M16 3v4"/></svg></span>
<span class="abs service-icon dark" style="left:418px;top:2322px"><svg viewBox="0 0 24 24"><circle cx="12" cy="13" r="8"/><path d="M12 9v4l3 2M10 2h4"/></svg></span>
<span class="abs service-icon" style="left:665px;top:2322px"><svg viewBox="0 0 24 24"><rect x="3" y="5" width="18" height="15" rx="2"/><path d="M3 9h18M8 3v4M16 3v4M9 15l2 2 4-4"/></svg></span>
<span class="abs service-icon" style="left:913px;top:2322px"><svg viewBox="0 0 24 24"><path d="M4 21V6h8v15M12 21V10h8v11M7 9h2M7 13h2M7 17h2M15 13h2M15 17h2M2 21h20"/></svg></span>
<a class="btn btn-dark" style="left:420px;top:2610px;width:114px;height:40px;border:3px solid var(--white)">Read More</a>

<!-- faq -->
<h2 class="abs display faq-title">FAQ for Our Dog Poop Removal Service</h2>
<div class="abs tabs">
  <span class="on">General Questions</span><span>Service Details</span><span>Pricing And Payments</span><span>Health And Safety</span><span>Customer Concerns</span><span>Additional Services</span>
</div>
<div class="abs faq-open">
  <div style="display:flex;justify-content:space-between;align-items:center"><h3>What does your dog poop removal service include?</h3><span class="caret down"></span></div>
  <p>Our service includes locating, scooping, and disposing of dog waste from your yard or designated area. We ensure your space is left clean and sanitary.</p>
</div>
<div class="abs faq-row" style="top:3169px"><h3>Do you service all yard sizes?</h3><span class="caret up"></span></div>
<div class="abs faq-row" style="top:3257px"><h3>How often can I schedule your services?</h3><span class="caret up"></span></div>
<div class="abs faq-row" style="top:3345px"><h3>Are you environmentally friendly?</h3><span class="caret up"></span></div>

<!-- call to action -->
<div class="abs cta-bg"></div>
<div class="visual cta-house" role="img" aria-label="Illustration of a brick cottage with a smoking chimney"></div>
<div class="visual cta-dog" role="img" aria-label="Cartoon dog mascot holding a pooper scooper in front of the house"></div>
<div class="abs cta-bush"></div>
<h2 class="abs display cta-title">Let's Keep Your<br>Yard Clean!"</h2>
<p class="abs cta-sub">Ready to schedule your cleanup or have questions?<br>We'd love to hear from you.</p>
<a class="btn btn-dark" style="left:116px;top:3825px;width:224px;height:43px">Click here for a Free Quote!</a>

<!-- footer -->
<svg class="abs footer" viewBox="0 0 1200 390" preserveAspectRatio="none" aria-hidden="true">
  <path d="M0 20 Q300 0 600 20 T1200 15 V380 Q900 395 600 385 T0 388 Z" fill="#7cc64a"/>
  <path d="M0 20 Q300 0 600 20 T1200 15 V60 Q600 45 0 60 Z" fill="#5aaa2e"/>
</svg>
<div class="abs foot-brand"><div class="dot"></div><span>The Fernwick Folks</span></div>
<div class="abs foot-col" style="left:377px;top:4068px">
  <h4>Quick Links</h4>
  <div class="foot-links">Home<br>About<br>Services<br>Contact Us<br>Client Portal<br>FAQ<br>Blog<br>Free Quote</div>
</div>
<div class="abs foot-col" style="left:626px;top:4068px">
  <h4>Contact Info</h4>
  <div class="contact"><span class="ic"><svg viewBox="0 0 24 24"><path d="M6 3l4 4-2 3c1 3 3 5 6 6l3-2 4 4-3 3C10 21 3 14 3 6z"/></svg></span><div><b>Phone</b><br>(555) 014-2287</div></div>
  <div class="contact"><span class="ic"><svg viewBox="0 0 24 24"><path d="M3 6h18v12H3zM3 6l9 7 9-7" fill="none" stroke="#fff" stroke-width="2"/></svg></span><div><b>Email</b><br>hello@fernwickfolks.example</div></div>
  <div class="contact"><span class="ic"><svg viewBox="0 0 24 24"><path d="M12 22s-7-7-7-12a7 7 0 0 1 14 0c0 5-7 12-7 12zm0-9a3 3 0 1 0 0-6 3 3 0 0 0 0 6z"/></svg></span><div><b>Address</b><br>4120 W Larkspur Ln,<br>Millbrook, ST 00000</div></div>
</div>
<div class="abs foot-col" style="left:945px;top:4068px">
  <h4>Contact Info</h4>
  <div class="socials" aria-label="Social media links"><span></span><span></span><span></span></div>
</div>
<p class="abs copyright">Copyright ©2025 The Fernwick Folks . All Rights Reserved</p>

</body>
</html>
```